Sleep Consulting Business

Hello I need a business card design with similar colors to my logo that was created. I help mom/parents whose little ones are having sleep issues. Are you able to recreate the picture with the girl sleeping onto a business card using a picture that I provide. That would be one side with my logo on top and on the other side would the following:
My name (in bigger letters than the rest. maybe written in script
title
email
website
phone
instagram
I have included color Inspo
Contact Information for Business Card
Full Name, number, email, website, ig page
Look and feel
Each slider illustrates characteristics of the customer's brand and the style your logo design should communicate.

```html
<!DOCTYPE html>
<html lang="en">
<head>
<meta charset="utf-8">
<title>Hushwell Sleep – Business Card</title>
<link rel="stylesheet" href="https://fonts.googleapis.com/css2?family=Montserrat:wght@400;500;600&family=Kaushan+Script&display=swap">
<style>
  :root {
    --backdrop: #ece7e2;
    --card-white: #ffffff;
    --ink-grey: #8a8282;
    --divider: #cfc9c6;
    --accent-peach: #d9977f;
    --icon-grey: #8f8787;
    --night-deep: #1c1a19;
    --night-mid: #2e2b29;
    --logo-light: #d8cfcb;
  }
  * { margin: 0; padding: 0; box-sizing: border-box; }
  html, body { width: 900px; height: 1200px; overflow: hidden; }
  body {
    background: var(--backdrop);
    font-family: "Montserrat", sans-serif;
    position: relative;
  }
  .card {
    position: absolute;
    left: 67px;
    width: 763px;
    height: 445px;
    border-radius: 30px;
    overflow: hidden;
  }
  .card-front { top: 107px; background: var(--card-white); }
  .card-back { top: 648px; }

  .brand-mark {
    position: absolute;
    display: flex;
    align-items: center;
    justify-content: center;
    gap: 12px;
    font-family: "Montserrat", sans-serif;
    font-weight: 500;
    white-space: nowrap;
  }
  .brand-mark-front {
    left: 40px;
    top: 196px;
    width: 330px;
    font-size: 32px;
    color: var(--ink-grey);
  }
  .brand-dot {
    flex: none;
    border-radius: 50%;
    background: var(--accent-peach);
  }
  .brand-mark-front .brand-dot { width: 22px; height: 22px; }

  .divider {
    position: absolute;
    left: 372px;
    top: 115px;
    width: 2px;
    height: 210px;
    background: var(--divider);
  }
  .contact-block {
    position: absolute;
    left: 411px;
    top: 110px;
  }
  .person-name {
    font-family: "Kaushan Script", cursive;
    font-weight: 400;
    font-size: 46px;
    line-height: 1.1;
    color: var(--ink-grey);
  }
  .person-title {
    margin-top: 6px;
    font-weight: 600;
    font-size: 19px;
    color: var(--accent-peach);
  }
  .contact-list { list-style: none; margin-top: 16px; }
  .contact-item {
    display: flex;
    align-items: center;
    gap: 9px;
    height: 30px;
    font-size: 17px;
    color: var(--ink-grey);
  }
  .contact-icon { width: 23px; height: 23px; flex: none; }

  .night-photo {
    position: absolute;
    inset: 0;
    background: radial-gradient(ellipse at 60% 45%, var(--night-mid) 0%, var(--night-deep) 75%);
  }
  .brand-mark-back {
    left: 0;
    right: 0;
    top: 190px;
    font-size: 48px;
    color: var(--logo-light);
    gap: 16px;
  }
  .brand-mark-back .brand-dot { width: 32px; height: 32px; }
</style>
</head>
<body>
  <section class="card card-front">
    <div class="brand-mark brand-mark-front"><span class="brand-dot"></span>Hushwell Sleep</div>
    <div class="divider"></div>
    <div class="contact-block">
      <h1 class="person-name">Jordan Reyes</h1>
      <p class="person-title">CEO/Founder</p>
      <ul class="contact-list">
        <li class="contact-item">
          <svg class="contact-icon" viewBox="0 0 24 24"><circle cx="12" cy="12" r="12" fill="var(--icon-grey)"/><path d="M8.5 6.5l2 2.2-1.2 1.5c.8 1.7 2 2.9 3.6 3.7l1.5-1.2 2.2 2-1.3 1.8c-4-.6-7.6-4.2-8.2-8.2z" fill="#fff"/></svg>
          555-014-2290
        </li>
        <li class="contact-item">
          <svg class="contact-icon" viewBox="0 0 24 24"><circle cx="12" cy="12" r="12" fill="var(--icon-grey)"/><rect x="6.5" y="8" width="11" height="8" fill="none" stroke="#fff" stroke-width="1.3"/><path d="M6.5 8l5.5 4.5L17.5 8" fill="none" stroke="#fff" stroke-width="1.3"/></svg>
          jordan@hushwell.com
        </li>
        <li class="contact-item">
          <svg class="contact-icon" viewBox="0 0 24 24"><circle cx="12" cy="12" r="12" fill="var(--icon-grey)"/><g fill="none" stroke="#fff" stroke-width="1.2"><circle cx="12" cy="12" r="6"/><ellipse cx="12" cy="12" rx="2.6" ry="6"/><path d="M6 12h12"/></g></svg>
          www.hushwellsleep.com
        </li>
        <li class="contact-item">
          <svg class="contact-icon" viewBox="0 0 24 24"><circle cx="12" cy="12" r="12" fill="var(--icon-grey)"/></svg>
          @hushwellsleep
        </li>
      </ul>
    </div>
  </section>

  <section class="card card-back">
    <div class="night-photo" role="img" aria-label="Dim photo of a child sleeping under a blanket"></div>
    <div class="brand-mark brand-mark-back"><span class="brand-dot"></span>Hushwell Sleep</div>
  </section>
</body>
</html>
```